Private Maths Tuition Flyer based in London

I am opening up a new Maths tuition centre in North West London. The flyer will be delivered to over 8,000 homes within the immediate vicinity. The design should be suitable to be printed on an A5 sheet and read in a portrait orientation.

The flyer should include the following:

The headline statement should be "Private Maths Tuition"

Secondary headline statement is the following "GCSE, A-Levels, 11 Plus exams"

Some of service offerings/selling points are:

- Free first session
- Monthly Feedback reports
- Free support outside of sessions
- Clear Target grades
- Personalised Lesson plans
- Tangible Results

Another statement that should be featured is "Book your free session by visiting www.lernova.co.uk" or something similar to that.

"Contact Details:
020 4719 8263
enquiries@lernova.co.uk"

"Address:
Kelbridge Business and Innovation Centre
Ashvale Court
Wrenfield Road
HA4 9QD"

Attached you'll see a logo which should be included and also a map of where we are. I am open to new images for the map if you guys have any, rather than a screen shot from google maps but it should be clear to see.

I would like the content above to be displayed in a clear and concise manner that is easy to read. You have creative license on where this information should be displayed and where the images should be but on the whole it should look aesthetically pleasing on the eye.

Target Market(s)

Students, Parents. Parents who want maths tutors.

Industry/Entity Type

Tutoring

Font styles to use
Sans Serif

Requirements
Must have
• *logo*
• Private Maths Tuition
• GCSE, A-Levels, 11 Plus exams
• - Free first session
• - Monthly Feedback reports
• - Free support outside of sessions
• - Clear Target grades
• - Personalised Lesson plans
• - Tangible Results
• Book your free session by visiting www.lernova.co.uk" or something similar to that.
• Contact Details:
• 020 4719 8263
• enquiries@lernova.co.uk
• Address (*with map*):
• Kelbridge Business and Innovation Centre
• Ashvale Court
• Wrenfield Road
• HA4 9QD
Nice to have
• similar colour scheme as the logo. creative background design.

```html
<!DOCTYPE html>
<html lang="en">
<head>
<meta charset="utf-8">
<title>Lernova – Private Maths Tuition Flyer</title>
<link rel="stylesheet" href="https://fonts.googleapis.com/css2?family=Roboto+Condensed:wght@700&family=Open+Sans:wght@400;600;700&display=swap">
<style>
  :root {
    --brand-blue: #1160ab;
    --brand-navy: #0d4f9a;
    --brand-green: #8cc63f;
    --brand-orange: #f07325;
    --ink: #2b2b2b;
    --grey: #444;
    --paper: #ffffff;
    --photo-dark: #5c3d24;
    --photo-light: #c9a47a;
    --map-base: #e9e6df;
    --map-park: #cfe3b8;
    --calc-tone: #b86a3c;
  }
  html, body {
    margin: 0;
    padding: 0;
    width: 901px;
    height: 1200px;
    overflow: hidden;
    background: #f2f2f2;
  }
  .flyer { display: block; width: 901px; height: 1200px; }
  .headline { font-family: "Roboto Condensed", "Arial Narrow", sans-serif; font-weight: 700; fill: #fff; }
  .headline-main { font-size: 68px; }
  .headline-sub { font-size: 42px; }
  .cta-badge-text { font-family: "Roboto Condensed", sans-serif; font-weight: 700; font-size: 46px; fill: #fff; }
  .brand-name { font-family: "Open Sans", sans-serif; font-weight: 400; font-size: 84px; fill: var(--brand-orange); }
  .contact-label { font-family: "Open Sans", sans-serif; font-size: 26px; fill: var(--grey); }
  .contact-phone { font-family: "Roboto Condensed", sans-serif; font-weight: 700; font-size: 44px; fill: var(--brand-navy); }
  .contact-email { font-family: "Roboto Condensed", sans-serif; font-weight: 700; font-size: 32px; fill: var(--brand-navy); }
  .offer-title { font-family: "Roboto Condensed", sans-serif; font-weight: 700; font-size: 33px; fill: var(--brand-navy); }
  .offer-item { font-family: "Open Sans", sans-serif; font-weight: 600; font-size: 22px; fill: var(--ink); }
  .offer-bullet { fill: none; stroke: var(--brand-blue); stroke-width: 4; }
  .cta-line { font-family: "Roboto Condensed", sans-serif; font-weight: 700; font-size: 42px; fill: #fff; }
  .address-line { font-family: "Open Sans", sans-serif; font-weight: 700; font-size: 23px; fill: #1a1a1a; }
</style>
</head>
<body>
<svg class="flyer" viewBox="0 0 901 1200" xmlns="http://www.w3.org/2000/svg">
  <defs>
    <linearGradient id="photoTone" x1="0" y1="0" x2="1" y2="1">
      <stop offset="0" stop-color="var(--photo-dark)"/>
      <stop offset="0.6" stop-color="var(--photo-light)"/>
      <stop offset="1" stop-color="#8a6040"/>
    </linearGradient>
    <radialGradient id="calcTone" cx="0.5" cy="0.5" r="0.5">
      <stop offset="0" stop-color="var(--calc-tone)"/>
      <stop offset="1" stop-color="#5b6f8c"/>
    </radialGradient>
    <linearGradient id="mapTone" x1="0" y1="0" x2="1" y2="1">
      <stop offset="0" stop-color="var(--map-park)"/>
      <stop offset="0.4" stop-color="var(--map-base)"/>
      <stop offset="1" stop-color="var(--map-base)"/>
    </linearGradient>
  </defs>

  <rect class="flyer-paper" width="901" height="1200" fill="var(--paper)"/>

  <!-- Header photo band -->
  <path role="img" aria-label="Photo of a hand writing maths equations on grid paper beside reading glasses"
        d="M0,0 H901 V352 C720,362 470,360 300,300 C180,255 80,215 0,185 Z" fill="url(#photoTone)"/>
  <path d="M0,185 C80,215 180,255 300,300 C470,360 720,362 901,352" fill="none" stroke="var(--brand-green)" stroke-width="9"/>
  <path d="M0,200 C90,240 190,280 310,318 C480,372 720,370 901,366" fill="none" stroke="var(--brand-blue)" stroke-width="7"/>

  <text class="headline headline-main" x="450" y="100" text-anchor="middle">PRIVATE MATHS TUITION</text>
  <text class="headline headline-sub" x="450" y="170" text-anchor="middle">GCSE, A-Levels, 11 Plus Exams</text>

  <!-- Book now badge -->
  <g class="cta-badge">
    <circle cx="743" cy="350" r="84" fill="var(--brand-green)"/>
    <circle cx="743" cy="350" r="76" fill="#fff"/>
    <circle cx="743" cy="350" r="71" fill="var(--brand-blue)"/>
    <text class="cta-badge-text" x="743" y="342" text-anchor="middle">BOOK</text>
    <text class="cta-badge-text" x="743" y="390" text-anchor="middle">NOW</text>
  </g>

  <!-- Brand and contact -->
  <text class="brand-name" x="215" y="525" text-anchor="middle">Lernova</text>
  <text class="contact-label" x="215" y="592" text-anchor="middle">CONTACT US:</text>
  <text class="contact-phone" x="215" y="638" text-anchor="middle">020 4719 8263</text>
  <text class="contact-email" x="215" y="683" text-anchor="middle">enquiries@lernova.co.uk</text>

  <!-- What we offer -->
  <line x1="447" y1="438" x2="447" y2="705" stroke="var(--brand-green)" stroke-width="2"/>
  <text class="offer-title" x="467" y="472">What We Offer</text>
  <line x1="447" y1="484" x2="820" y2="484" stroke="var(--brand-green)" stroke-width="2"/>
  <g class="offer-list">
    <circle class="offer-bullet" cx="478" cy="511" r="6"/><text class="offer-item" x="495" y="519">Free first session</text>
    <circle class="offer-bullet" cx="478" cy="548" r="6"/><text class="offer-item" x="495" y="556">Monthly Feedback reports</text>
    <circle class="offer-bullet" cx="478" cy="585" r="6"/><text class="offer-item" x="495" y="593">Free support outside of sessions</text>
    <circle class="offer-bullet" cx="478" cy="622" r="6"/><text class="offer-item" x="495" y="630">Clear Target grades</text>
    <circle class="offer-bullet" cx="478" cy="659" r="6"/><text class="offer-item" x="495" y="667">Personalised Lesson plans</text>
    <circle class="offer-bullet" cx="478" cy="696" r="6"/><text class="offer-item" x="495" y="704">Tangible Results</text>
  </g>

  <!-- Orange footer band -->
  <path d="M0,700 C130,790 300,885 480,922 C540,934 600,940 640,942 V1200 H0 Z" fill="var(--brand-orange)"/>
  <path d="M0,660 C130,760 300,860 480,900 C540,912 600,918 640,920" fill="none" stroke="var(--brand-blue)" stroke-width="9"/>
  <path d="M0,680 C130,776 300,872 480,912" fill="none" stroke="var(--brand-green)" stroke-width="7"/>

  <!-- Calculator illustration medallion -->
  <circle cx="206" cy="815" r="113" fill="var(--brand-green)"/>
  <circle cx="206" cy="815" r="102" fill="#fff"/>
  <circle role="img" aria-label="Illustration of a calculator with a pencil and worksheets" cx="206" cy="815" r="94" fill="url(#calcTone)"/>

  <!-- Location map in heart frame -->
  <path d="M720,1200 C600,1100 466,960 476,860 C486,778 556,736 630,741 C690,746 722,772 742,790 C772,760 822,736 872,741 L901,746 V1200 Z"
        fill="none" stroke="var(--brand-blue)" stroke-width="12"/>
  <path role="img" aria-label="Street map showing the Kelbridge Business and Innovation Centre location"
        d="M720,1200 C604,1104 476,962 486,862 C496,786 560,748 630,752 C688,757 718,782 742,802 C772,772 822,748 872,752 L901,756 V1200 Z"
        fill="url(#mapTone)"/>

  <!-- Footer text -->
  <text class="cta-line" x="50" y="1018">BOOK YOUR FREE</text>
  <text class="cta-line" x="50" y="1066">SESSION BY VISITING</text>
  <text class="cta-line" x="50" y="1114">www.lernova.co.uk</text>
  <text class="address-line" x="50" y="1132" dy="0" visibility="hidden"> </text>
  <text class="address-line" x="50" y="1158">Kelbridge Business and Innovation Centre</text>
  <text class="address-line" x="50" y="1191">Ashvale Court, Wrenfield Road, HA4 9QD</text>
</svg>
</body>
</html>
```